limo company looking for a graphic business card with professional look and feel

Looking for a business card design that can give you the full picture of the limo company by looking at the card - we provide airport service, wedding, birthday, night out, etc... we have sedans, suvs , limos, and party buses. I want the business card to have a professional look because we are targetting corporate clients as well as regular retail.
Info about the business can be found at: http://qivroe.example/Tm3Kx7
Target Market(s)
corporate clients and retail
Industry/Entity Type
Business
Contact Information for Business Card
I would like the logo and the name of the company to be in raised print - not sure if design makes a difference for that or just print - I need it designed in 350dpi
Requirements
Must have
- pictures of vehicle types (sedans, suvs, limos, party bus). pictures of interior of the limos if possible. list service types (weddings, birthdays, proms, airport transportation) & service areas (houston, the woodlands, spring, tomball, cypress, kingwood).
Nice to have
- nice professional look to it.

```html
<!DOCTYPE html>
<html lang="en">
<head>
<meta charset="utf-8">
<title>Velmont Limousine &amp; Transportation – Business Card</title>
<link href="https://fonts.googleapis.com/css2?family=Didact+Gothic&display=swap" rel="stylesheet">
<style>
  :root {
    --backdrop: #161616;
    --card-top: #2e2e2e;
    --card-bottom: #0c0c0c;
    --ink: #c9c9c9;
    --ink-soft: #9a9a9a;
    --rule: #d8d8d8;
    --band: #1f2326;
  }
  * { margin: 0; padding: 0; box-sizing: border-box; }
  html, body { width: 1200px; height: 936px; overflow: hidden; background: var(--backdrop); }
  body { font-family: "Didact Gothic", "Century Gothic", sans-serif; color: var(--ink); }
  .sheet { position: relative; width: 1200px; height: 936px; }
  .card {
    position: absolute; left: 250px; width: 700px; height: 400px;
    background: linear-gradient(160deg, var(--card-top), var(--card-bottom) 70%);
    overflow: hidden; box-shadow: 0 10px 30px rgba(0,0,0,.6);
  }
  .card--services { top: 48px; }
  .card--contact { top: 488px; }

  /* services side */
  .photo-band { position: absolute; left: 0; top: 0; width: 700px; height: 160px; }
  .service-types { position: absolute; left: 60px; top: 176px; font-size: 19px; line-height: 28px; }
  .service-types h2, .service-areas h2 { font-weight: 400; font-size: 19px; text-decoration: underline; text-underline-offset: 4px; }
  .service-types ul { list-style: none; }
  .service-types li:nth-child(2) { padding-left: 60px; }
  .service-types li:nth-child(3) { padding-left: 30px; }
  .service-areas { position: absolute; left: 420px; top: 176px; font-size: 19px; line-height: 28px; }
  .service-areas ul { display: grid; grid-template-columns: 150px 110px; list-style: none; }
  .brand { position: absolute; text-align: left; color: var(--ink); white-space: nowrap; }
  .brand__name { font-size: 26px; letter-spacing: .5px; display: flex; align-items: center; gap: 10px; line-height: 32px; }
  .brand__mark { width: 12px; height: 12px; background: var(--ink); border-radius: 50%; }
  .brand__sub { font-size: 16px; line-height: 20px; color: var(--ink-soft); padding-left: 22px; }
  .card--services .brand { left: 360px; top: 304px; }
  .rule-bottom { position: absolute; left: 0; right: 0; top: 370px; height: 1px; background: var(--rule); opacity: .8; }

  /* contact side */
  .vehicle-photo { position: absolute; left: 0; top: 60px; width: 360px; height: 340px; }
  .card--contact .brand { right: 40px; top: 40px; }
  .contact { position: absolute; right: 40px; top: 130px; text-align: right; font-size: 16px; line-height: 26px; }
  .contact li { list-style: none; display: flex; justify-content: flex-end; align-items: center; gap: 8px; }
  .contact svg { width: 14px; height: 14px; }
  .address { margin-top: 12px; }
</style>
</head>
<body>
<main class="sheet">
  <section class="card card--services">
    <svg class="photo-band" viewBox="0 0 700 160">
      <defs>
        <linearGradient id="cabinA" x1="0" y1="0" x2="1" y2="1"><stop offset="0" stop-color="#3b2c4a"/><stop offset="1" stop-color="#14121c"/></linearGradient>
        <linearGradient id="cabinB" x1="0" y1="0" x2="1" y2="1"><stop offset="0" stop-color="#4c5b8a"/><stop offset="1" stop-color="#161b2c"/></linearGradient>
        <linearGradient id="cabinC" x1="0" y1="0" x2="1" y2="1"><stop offset="0" stop-color="#5a5a5a"/><stop offset="1" stop-color="#1a1a1a"/></linearGradient>
        <linearGradient id="cabinD" x1="0" y1="0" x2="1" y2="1"><stop offset="0" stop-color="#a9adb4"/><stop offset="1" stop-color="#4a3a56"/></linearGradient>
      </defs>
      <rect width="700" height="150" fill="var(--band)"/>
      <polygon points="60,150 120,60 260,60 200,150" fill="url(#cabinA)" stroke="#ddd" stroke-width="1.5" role="img" aria-label="Photo: party bus interior with purple lighting"/>
      <polygon points="210,150 270,60 410,60 350,150" fill="url(#cabinB)" stroke="#ddd" stroke-width="1.5" role="img" aria-label="Photo: limousine cabin with blue lighting"/>
      <polygon points="360,150 420,60 540,60 480,150" fill="url(#cabinC)" stroke="#ddd" stroke-width="1.5" role="img" aria-label="Photo: leather seats of a sedan interior"/>
      <polygon points="490,150 550,20 700,20 700,150" fill="url(#cabinD)" stroke="#ddd" stroke-width="1.5" role="img" aria-label="Photo: stretch limousine interior with bar"/>
      <line x1="0" y1="152" x2="700" y2="152" stroke="var(--rule)" stroke-width="1.5"/>
    </svg>
    <div class="service-types">
      <h2>Our Service Types</h2>
      <ul>
        <li>Weddings &amp; Birthdays</li>
        <li>Proms</li>
        <li>Airport transportation</li>
      </ul>
    </div>
    <div class="service-areas">
      <h2>Our Service Areas</h2>
      <ul>
        <li>Houston</li><li>Cypress</li>
        <li>The Woodlands</li><li>Kingwood</li>
        <li>Spring</li><li>Tomball</li>
      </ul>
    </div>
    <div class="brand">
      <div class="brand__name"><span class="brand__mark"></span>Velmont Limousine</div>
      <div class="brand__sub">&amp; Transportation</div>
    </div>
    <div class="rule-bottom"></div>
  </section>

  <section class="card card--contact">
    <svg class="vehicle-photo" viewBox="0 0 360 340" role="img" aria-label="Photo: black SUV, three-quarter front view">
      <defs>
        <radialGradient id="suv" cx=".55" cy=".45" r=".6"><stop offset="0" stop-color="#3c3c3c"/><stop offset="1" stop-color="#0d0d0d"/></radialGradient>
      </defs>
      <rect width="360" height="340" fill="url(#suv)"/>
    </svg>
    <div class="brand">
      <div class="brand__name"><span class="brand__mark"></span>Velmont Limousine</div>
      <div class="brand__sub">&amp; Transportation</div>
    </div>
    <ul class="contact">
      <li>800-555-0182
        <svg viewBox="0 0 14 14"><path d="M3 1l2 3-1.5 1.5a8 8 0 0 0 5 5L10 9l3 2-1 2c-6 0-11-5-11-11z" fill="var(--ink)"/></svg>
      </li>
      <li>832-555-0147
        <svg viewBox="0 0 14 14"><path d="M3 1l2 3-1.5 1.5a8 8 0 0 0 5 5L10 9l3 2-1 2c-6 0-11-5-11-11z" fill="var(--ink)"/></svg>
      </li>
      <li>service@velmontlimo.example
        <svg viewBox="0 0 14 14"><rect x="1" y="3" width="12" height="8" fill="none" stroke="var(--ink)"/><path d="M1 3l6 5 6-5" fill="none" stroke="var(--ink)"/></svg>
      </li>
      <li class="address">4 Cedar Point Plaza</li>
      <li>2150 Cedar Point Blvd, Suite #300</li>
      <li>The Woodlands, TX 77381</li>
    </ul>
  </section>
</main>
</body>
</html>
```